I am writing a book called "SMILING OPENS EVERY DOOR "

I NEED A BOOK COVER FOR MY BOOK" SMILING OPENS EVERY DOOR"
so what was the question? " ( this in smaller font)

"Smiling Opens Every Door " will need to designed to eventually be a logo , banner and business card
COLOURS MAINLY ORANGE AND WHITE (with accents bright colour )

THE BOOK IS MY LAUGHTER JOURNEY AS A PERFORMER AND ADVENTURE INDIA LEARNING ABOUT LAUGHTER YOGA WHICH I WILL BE TEACHING

I do not want photos on the front cover ..
The look could be modern and eye-catching
I have also just been to India to learn Laughing Yoga with Dr Tobin Verhaal

Thank-you so much everyone for your brilliant designs . i am overwhelmed with your talent . i hope to work with you all again soon ! Marnie  

Target Market(s)

"Adults based in western speaking countries aged 25 to 60 that want to learn to laugh more
Also this book will be sold at my conference workshops

Industry/Entity Type

Business

Requirements
Must have
• ORANGE AND WHITE
CAN HAVE AQUA , HOT PINK , LIME GREEN, YELLOW ACCENTS

THESE WILL BE DIFFERENT AREAS WILL COVERING IN MY BOOK
EG LAUGHTER NAD BREAT CANCER ( PINK)
LAUGHTER NAD DEPRESSION ( BLUE)
LAUGHTER AND KIDS ( YELLOW)

NO Photos on front cover
Should not have
• No photos

```html
<!DOCTYPE html>
<html lang="en">
<head>
<meta charset="UTF-8">
<title>Smiling Opens Every Door — Book Cover</title>
<link rel="stylesheet" href="https://fonts.googleapis.com/css2?family=Arimo:wght@700&display=swap">
<style>
  :root {
    --cover-white: #ffffff;
    --accent-aqua: #00aeef;
    --brand-orange: #f26a2e;
    --brand-orange-soft: #f7a27a;
    --text-white: #ffffff;
  }
  * { margin: 0; padding: 0; box-sizing: border-box; }
  html, body {
    width: 750px;
    height: 1200px;
    overflow: hidden;
    background: var(--cover-white);
  }
  .book-cover {
    position: relative;
    width: 750px;
    height: 1200px;
    background: var(--cover-white);
    font-family: "Arimo", Arial, Helvetica, sans-serif;
    font-weight: 700;
    overflow: hidden;
  }
  .top-band {
    position: absolute;
    top: 0; left: 0;
    width: 750px;
    height: 52px;
    background: var(--accent-aqua);
  }
  .title-art {
    position: absolute;
    top: 0; left: 0;
    width: 750px;
    height: 1200px;
  }
  .title-main {
    fill: var(--brand-orange);
    font-family: "Arimo", Arial, Helvetica, sans-serif;
    font-weight: 700;
    font-size: 118px;
    letter-spacing: 6px;
  }
  .title-sub {
    fill: var(--brand-orange);
    font-family: "Arimo", Arial, Helvetica, sans-serif;
    font-weight: 700;
    font-size: 94px;
  }
  .figure-stop-core { stop-color: var(--brand-orange); }
  .figure-stop-edge { stop-color: var(--brand-orange-soft); }
  .figure-accent { fill: var(--accent-aqua); }
  .author-tag {
    position: absolute;
    left: 250px;
    bottom: 0;
    width: 500px;
    height: 62px;
    background: var(--accent-aqua);
    color: var(--text-white);
    font-size: 31px;
    line-height: 62px;
    text-align: center;
  }
</style>
</head>
<body>
  <main class="book-cover">
    <div class="top-band"></div>

    <svg class="title-art" viewBox="0 0 750 1200" xmlns="http://www.w3.org/2000/svg">
      <defs>
        <path id="upper-arc" d="M33,600 A342,342 0 0 1 717,600"/>
        <path id="lower-arc" d="M-25,600 A400,400 0 0 0 775,600"/>
        <radialGradient id="figure-tone" cx="50%" cy="55%" r="60%">
          <stop offset="0%" class="figure-stop-core"/>
          <stop offset="100%" class="figure-stop-edge"/>
        </radialGradient>
      </defs>

      <text class="title-main" text-anchor="middle">
        <textPath href="#upper-arc" startOffset="50%">SMILING</textPath>
      </text>

      <g role="img" aria-label="Flat orange illustration of a person seated cross-legged in a meditation pose, hands raised, with aqua accents">
        <ellipse cx="378" cy="560" rx="255" ry="250" fill="url(#figure-tone)"/>
      </g>

      <text class="title-sub" text-anchor="middle">
        <textPath href="#lower-arc" startOffset="50%">Opens Every Door</textPath>
      </text>
    </svg>

    <div class="author-tag">by: Author’s Name Here</div>
  </main>
</body>
</html>
```